Diesel Fitting/Mechanical Company Needs a new Business Card

We would like a new business card that showcases our logo and business information.

Industry/Entity Type

Business

Contact Information for Business Card

314 Wendale Street
PO Box 7581 KELLAWAY QLD 4891
Phone: 49312787 Fax: 49312688 Mobile: 0438915276 ABN: 63 519 087 342

Requirements
Must have
• The following email addresses:
• admin@tkservicing.com.au , sales@tkservicing.com.au , accounts@tkservicing.com.au , parts@tkservicing.com.au , office@tkservicing.com.au
• Also need to have the website: www.tkservicing.com.au

```html
<!DOCTYPE html>
<html lang="en">
<head>
<meta charset="utf-8">
<title>TK Servicing Business Card</title>
<link rel="stylesheet" href="https://fonts.googleapis.com/css2?family=Open+Sans:wght@400;600&display=swap">
<style>
  :root {
    --backdrop: #3b3b3d;
    --card: #141415;
    --ink: #f2f2f2;
    --accent: #f07f1e;
    --rule: #2c2c2e;
  }
  html, body {
    margin: 0;
    width: 1200px;
    height: 900px;
    overflow: hidden;
    background: var(--backdrop);
    font-family: "Open Sans", Arial, sans-serif;
  }
  .card {
    position: absolute;
    left: 150px;
    top: 193px;
    width: 900px;
    height: 514px;
    background: var(--card);
    border-radius: 26px;
    box-shadow: 0 10px 30px rgba(0,0,0,0.35);
    color: var(--ink);
  }
  .brand {
    position: absolute;
    left: 70px;
    top: 200px;
    display: flex;
    align-items: center;
    gap: 16px;
  }
  .brand-dot {
    width: 38px;
    height: 38px;
    border-radius: 50%;
    background: var(--accent);
  }
  .brand-name {
    font-size: 46px;
    font-weight: 600;
    color: var(--accent);
    letter-spacing: 0.5px;
  }
  .contact {
    position: absolute;
    left: 450px;
    top: 44px;
    padding-left: 34px;
    border-left: 1px solid var(--rule);
    height: 330px;
  }
  .contact ul {
    list-style: none;
    margin: 0;
    padding: 0;
  }
  .contact li {
    display: flex;
    align-items: center;
    gap: 14px;
    font-size: 21px;
    line-height: 30px;
  }
  .contact svg {
    width: 17px;
    height: 17px;
    flex: none;
    fill: var(--accent);
  }
  .abn {
    margin: 12px 0 18px;
    font-size: 21px;
    line-height: 30px;
  }
  .abn-label {
    color: var(--accent);
    font-weight: 600;
  }
  .address {
    position: absolute;
    left: 70px;
    bottom: 40px;
    margin: 0;
    font-size: 25px;
    font-weight: 600;
    letter-spacing: 0.2px;
  }
</style>
</head>
<body>
  <section class="card">
    <div class="brand">
      <span class="brand-dot"></span>
      <span class="brand-name">TK Servicing</span>
    </div>

    <div class="contact">
      <ul class="phones">
        <li>
          <svg viewBox="0 0 24 24" aria-hidden="true"><path d="M6.6 10.8a15 15 0 0 0 6.6 6.6l2.2-2.2a1 1 0 0 1 1-.25 11.4 11.4 0 0 0 3.6.57 1 1 0 0 1 1 1V20a1 1 0 0 1-1 1A17 17 0 0 1 3 4a1 1 0 0 1 1-1h3.5a1 1 0 0 1 1 1c0 1.25.2 2.45.57 3.57a1 1 0 0 1-.25 1z"/></svg>
          49312787
        </li>
        <li>
          <svg viewBox="0 0 24 24" aria-hidden="true"><path d="M6 2h9l3 3v4H6zM3 10h18v9h-3v3H6v-3H3zm5 6v4h8v-4z"/></svg>
          49312688
        </li>
        <li>
          <svg viewBox="0 0 24 24" aria-hidden="true"><path d="M7 1h10a2 2 0 0 1 2 2v18a2 2 0 0 1-2 2H7a2 2 0 0 1-2-2V3a2 2 0 0 1 2-2zm0 4v13h10V5zm5 14.5a1 1 0 1 0 0 2 1 1 0 0 0 0-2z"/></svg>
          0438915276
        </li>
      </ul>

      <div class="abn"><span class="abn-label">ABN:</span> 63 519 087 342</div>

      <ul class="emails">
        <li><svg viewBox="0 0 24 24" aria-hidden="true"><path d="M2 5h20v14H2zm2 2v.5l8 5 8-5V7z"/></svg>admin@tkservicing.com.au</li>
        <li><svg viewBox="0 0 24 24" aria-hidden="true"><path d="M2 5h20v14H2zm2 2v.5l8 5 8-5V7z"/></svg>sales@tkservicing.com.au</li>
        <li><svg viewBox="0 0 24 24" aria-hidden="true"><path d="M2 5h20v14H2zm2 2v.5l8 5 8-5V7z"/></svg>accounts@tkservicing.com.au</li>
        <li><svg viewBox="0 0 24 24" aria-hidden="true"><path d="M2 5h20v14H2zm2 2v.5l8 5 8-5V7z"/></svg>parts@tkservicing.com.au</li>
        <li><svg viewBox="0 0 24 24" aria-hidden="true"><path d="M2 5h20v14H2zm2 2v.5l8 5 8-5V7z"/></svg>office@tkservicing.com.au</li>
        <li><svg viewBox="0 0 24 24" aria-hidden="true"><circle cx="12" cy="12" r="9" fill="none" stroke="currentColor"/><path d="M12 2a10 10 0 1 0 0 20 10 10 0 0 0 0-20zm0 2c.9 0 2.2 1.9 2.7 5H9.3C9.8 5.9 11.1 4 12 4zM4.3 11h4.8c0 .7 0 1.4.1 2H4.3a8 8 0 0 1 0-2zm.7 4h4.4c.4 1.7 1 3.1 1.7 4A8 8 0 0 1 5 15zm2-6H5a8 8 0 0 1 6.1-4C10.4 5.9 9.8 7.3 9.4 9zm5 10c-.9 0-2.2-1.5-2.7-4h5.4c-.5 2.5-1.8 4-2.7 4zm-1-6-.1-2h4.2c.1.6.1 1.4 0 2zm3.6 6c.7-.9 1.3-2.3 1.7-4H19a8 8 0 0 1-4.4 4zm2.3-6c.1-.6.1-1.3 0-2h2.8a8 8 0 0 1 0 2zm-.3-4c-.4-1.7-1-3.1-1.7-4A8 8 0 0 1 19 9z"/></svg>website: www.tkservicing.com.au</li>
      </ul>
    </div>

    <p class="address">314 Wendale Street PO Box 7581 KELLAWAY QLD 4891</p>
  </section>
</body>
</html>
```